HTML Web layout / data visualization for an information software application

We have a product used by patent analysts to allow them examine information stored in patents - particularly those patents that include biological sequences like DNA, RNA, and protein.

When the user opens up a particular patent, they currently see a very poorly organized wall of text, presenting fields of data to them in unorganized ways. We have attached screenshots of the current interface.

The project is to redesign that layout so that the same information is presented in a way which is brings important data to the the eyes of the user, categorizes data appropriately, and is visually appealing. We have proposed logical categorizations of data in the document called "Fields documentation."

The deliverable should be an HTML5 file that renders one or more of the examples of records we've provided in your new design.

Description of files:

"Examples of records badly displayed": MS Word file that shows three different examples of the records we would like to better visualize.

"screengrab1.tiff" and "screengrab2.tiff": pictures of how these records sit inside of our product. This is presented to give you a sense of screen real estate, our look and feel, and colors. We do not want the whole screen redesigned - just the record display itself.

"Fields documentation": detailed documentation of what each field means. We have tried to group them logically for you, and have also attempted to inform you as to which fields are linked to others.

Hi all,

Thanks for the designs so far. Unfortunately, nearly every design fails to understand the nature of the project. The problem we have is not about fonts and colors (although those matter). It is about grouping information together and displaying data in a way that provides insight. In the original brief, we say:

The document we have uploaded called "Fields documentation" is the most important document. We sense that very few of you have taken it into account. It provides notes on the nature of the data in the report and gives signs of the ways in which a creative designer might help to arrange the content.

Thanks for your consideration of this project.

TB

Target Market(s)

Patent analysts, heavily educated scientists, Ph.Ds.

Industry/Entity Type

Software

```html
<!DOCTYPE html>
<html lang="en">
<head>
<meta charset="utf-8">
<title>TideBase – Subject Annotation</title>
<link href="https://fonts.googleapis.com/css2?family=Arimo:wght@400;700&family=Noto+Sans:wght@400;600;700&display=swap" rel="stylesheet">
<style>
:root{
  --blue:#2b7bb9;
  --link:#1f6fb2;
  --head:#0a6a9e;
  --head-dark:#1b4d6e;
  --tab:#236e95;
  --tab-active:#173c55;
  --ink:#222;
  --muted:#555;
  --line:#c9c9c9;
  --panel:#dedede;
  --panel-in:#e4e4e4;
  --row2:#f0f0f0;
  --bar:#f4f4f4;
  --white:#fff;
}
*{box-sizing:border-box;margin:0;padding:0}
html,body{width:1200px;height:949px;overflow:hidden;background:var(--white)}
body{position:relative;font-family:"Arimo",Arial,sans-serif;color:var(--ink);font-size:13px}
.abs{position:absolute}
a,.lnk{color:var(--link);text-decoration:none}
.ui{font-family:"Noto Sans",Verdana,sans-serif}

.brand{left:10px;top:34px;display:flex;align-items:center;gap:8px;font:700 24px "Noto Sans",sans-serif;color:var(--blue)}
.brand-dot{width:28px;height:28px;border-radius:50%;background:var(--blue)}
.topnav{right:14px;top:54px;font-size:11.5px;display:flex;gap:14px}
.crumbs{left:12px;top:85px;font-size:11px}
.crumbs b{font-weight:700}
.crumb-help{right:12px;top:85px;font-size:11px}
.sq{display:inline-block;width:7px;height:7px;border:1px solid #999;margin-right:6px}

.toolbar{left:9px;top:102px;width:1178px;height:85px;border:1px solid var(--line);background:var(--bar)}
.menu{position:absolute;left:0;top:0;right:0;height:30px;border-bottom:1px solid var(--line);display:flex;font-size:13px;padding:9px 0 0 11px}
.menu span{margin-right:17px}
.selcount{position:absolute;right:8px;top:9px;font-size:11.5px}
.btn{position:absolute;top:37px;height:40px;border:1px solid #bcbcbc;border-radius:2px;background:linear-gradient(#fff,#e6e6e6);display:flex;align-items:center;gap:7px;padding:0 10px;font-size:13px}
.btn svg{flex:none}
.caret{width:0;height:0;border-left:4px solid transparent;border-right:4px solid transparent;border-top:5px solid #555}

.resline{top:202px;font-size:11.5px}
.table{left:15px;top:228px;width:1172px}
.thead{height:39px;background:var(--head);color:#fff;font-size:11.5px;display:flex}
.thead div{border-right:1px solid #5aa0c6;text-align:center;line-height:12px}
.row{height:39px;display:flex;align-items:center;font-size:12px}
.row.r1{background:linear-gradient(#f2f2f2,#d8d8d8)}
.row.r2{background:var(--row2)}
.cb{width:13px;height:13px;border:1px solid #888;background:#fff;border-radius:2px}
.c1{width:35px;display:flex;justify-content:center}
.c2{width:60px;padding-left:10px}.c3{width:60px;padding-left:10px}.c4{width:58px;padding-left:8px}
.c5{width:70px;padding-left:6px}.c6{width:85px;padding-left:16px}.c7{width:85px;padding-left:15px}
.c8{width:128px;padding-left:9px}.c9{flex:1;padding-left:9px}

.tabs{left:15px;top:353px;height:38px;display:flex;font-size:13px;color:#fff}
.tabs div{background:var(--tab);padding:12px 10px 0}
.tabs .on{background:var(--tab-active)}
.tabs .first{padding-left:20px;border-radius:6px 0 0 0}
.tabs .last{border-radius:0 6px 0 0;padding-right:14px}
.idline{left:474px;top:364px;font-size:13px;display:flex;align-items:center;gap:6px}
.info{width:16px;height:16px;border-radius:50%;background:#3e9be0;color:#fff;font:700 11px Arial;text-align:center;line-height:16px}

.detail{left:15px;top:391px;width:1172px;height:493px;background:var(--panel)}
.inner{left:28px;top:407px;width:820px;height:442px;background:var(--panel-in)}
.rail{left:143px;top:450px;width:1px;height:358px;background:#555}
.nav{left:0;width:134px;font-size:11.5px;text-align:right;white-space:nowrap}
.nav.on{color:var(--link)}
.dot{left:140px;width:7px;height:7px;border-radius:50%;background:var(--head)}
.scroll{left:847px;top:438px;width:4px;height:393px;background:#bdbdbd;border-radius:2px}
.thumb{left:846px;top:480px;width:6px;height:108px;background:var(--head);border-radius:3px}

.f{left:164px;font-size:13.3px;white-space:nowrap}
.lab{color:var(--link)}
.col{position:absolute;left:175px}
.val{position:absolute;left:185px;white-space:nowrap;line-height:26px;top:-6px}

.side{left:875px;top:406px;width:300px;height:456px;background:var(--white);padding:10px 14px;font-size:11.5px;line-height:25px}
</style>
</head>
<body>

<div class="abs brand"><span class="brand-dot"></span>TideBase</div>
<div class="abs topnav ui lnk"><span>Quick Launch ▾</span><span>Brieflab Competition ▾</span><span>Help ▾</span></div>
<div class="abs crumbs ui"><span class="sq"></span><a>Home</a> &gt; <a>Sample result for the Brieflab Competition</a> &gt; <b class="lnk">Full aln results of workflow Sample result for the Brieflab Competition</b></div>
<div class="abs crumb-help ui lnk">Help on this page</div>

<div class="abs toolbar">
  <div class="menu"><span>Result</span><span>View</span><span>Export</span><span>Applications</span></div>
  <div class="selcount ui">0 results selected <span class="lnk">[x]</span></div>
  <div class="btn" style="left:9px;width:128px"><svg width="24" height="22" viewBox="0 0 24 22"><rect x="1" y="2" width="20" height="16" fill="#fff" stroke="#667"/><rect x="1" y="2" width="20" height="4" fill="#8aa"/><circle cx="15" cy="13" r="4" fill="none" stroke="#333" stroke-width="1.5"/><line x1="18" y1="16" x2="22" y2="20" stroke="#333" stroke-width="2"/></svg><b>Filtering</b><span class="caret"></span></div>
  <div class="btn" style="left:146px;width:128px"><svg width="22" height="22" viewBox="0 0 22 22"><ellipse cx="11" cy="4" rx="9" ry="3" fill="#ccc" stroke="#666"/><path d="M2 4v14c0 2 18 2 18 0V4" fill="#ccc" stroke="#666"/><path d="M2 9c0 2 18 2 18 0M2 14c0 2 18 2 18 0" fill="none" stroke="#666"/></svg>Grouping<span class="caret"></span></div>
  <div class="btn" style="left:283px;width:116px"><svg width="22" height="24" viewBox="0 0 22 24"><path d="M6 2v18M2 16l4 5 4-5" stroke="#2b6ea8" stroke-width="2.5" fill="none"/><text x="12" y="10" font-size="9" font-family="Arial" fill="#2b6ea8">A</text><text x="12" y="22" font-size="9" font-family="Arial" fill="#2b6ea8">Z</text></svg>Sorting<span class="caret"></span></div>
  <div class="btn" style="left:408px;width:121px"><svg width="24" height="22" viewBox="0 0 24 22"><circle cx="5" cy="11" r="4" fill="#2b7bb9"/><circle cx="19" cy="4" r="3.5" fill="#2b7bb9"/><circle cx="19" cy="18" r="3.5" fill="#2b7bb9"/><path d="M5 11L19 4M5 11l14 7" stroke="#2b7bb9" stroke-width="2"/></svg>Sharing<span class="caret"></span></div>
  <div class="btn" style="left:590px;width:139px;font-size:11.5px"><svg width="26" height="26" viewBox="0 0 26 26"><circle cx="13" cy="13" r="11" fill="none" stroke="#2b7bb9" stroke-width="2"/></svg>Export to Arbor</div>
</div>

<div class="abs resline ui" style="left:10px">Results are ungrouped</div>
<div class="abs resline ui" style="left:440px"><span style="color:#888">&lt;&lt; First &lt; Previous</span>&nbsp;&nbsp; Results 1-50 of 500 &nbsp;&nbsp;<span class="lnk">Next &gt; Last &gt;&gt;</span></div>
<div class="abs resline ui" style="right:13px">500 Results</div>

<div class="abs table">
  <div class="thead ui">
    <div class="c1" style="flex-direction:column;align-items:center;gap:2px;padding-top:4px"><span class="cb" style="background:var(--head-dark);border-color:#fff"></span><span class="cb"></span></div>
    <div class="c2" style="padding:5px 0 0">Query %<br>Id</div><div class="c3" style="padding:5px 0 0">Subj. %<br>Id</div><div class="c4" style="padding:5px 0 0">Align %<br>Id</div>
    <div class="c5" style="padding:5px 0 0">E-val</div><div class="c6" style="padding:5px 0 0">Query<br>Identifier</div><div class="c7" style="padding:5px 0 0">Query<br>Identifier</div>
    <div class="c8" style="padding:5px 0 0">Identifier</div><div class="c9" style="padding:5px 0 0;border:0">Description / Title</div>
  </div>
  <div class="row r1"><div class="c1"><span class="cb"></span></div><div class="c2">98.9</div><div class="c3">9.03</div><div class="c4">99.72</div><div class="c5">8.90e-216</div><div class="c6">seq_1</div><div class="c7">seq_1</div><div class="c8">EP2539456-0043</div><div class="c9">INCREASING PLANT GROWTH BY MODULATING OMEGA-AMIDASE EXPRESSION IN PLANTS</div></div>
  <div class="row r2"><div class="c1"><span class="cb"></span></div><div class="c2">98.9</div><div class="c3">9.03</div><div class="c4">99.72</div><div class="c5">8.90e-216</div><div class="c6">seq_1</div><div class="c7">seq_1</div><div class="c8">US6812339-13070</div><div class="c9">POLYCOMB-ASSOCIATED NON-CODING RNAS</div></div>
</div>

<div class="abs tabs"><div class="first">Alignment</div><div class="on">Subject Annotation</div><div>Subject Sequence</div><div class="last">Query Sequence</div></div>
<div class="abs idline"><span class="info">i</span>Identifier &nbsp;: <span class="lnk">US6812339-13070</span><span style="margin:0 22px 0 26px">|</span><span style="color:var(--muted)">Patent Number :</span> <span class="lnk">US6812339</span></div>

<div class="abs detail"></div>
<div class="abs inner"></div>
<div class="abs rail"></div>
<div class="abs nav on" style="top:449px">Patent &amp; invention</div>
<div class="abs nav" style="top:490px">Priority &amp; legal status</div>
<div class="abs nav" style="top:531px">Claims</div>
<div class="abs nav" style="top:572px">Biological sequence</div>
<div class="abs nav" style="top:613px">Dates</div>
<div class="abs nav" style="top:653px">Miscellaneous</div>
<div class="abs dot" style="top:453px"></div><div class="abs dot" style="top:494px"></div><div class="abs dot" style="top:535px"></div>
<div class="abs dot" style="top:576px"></div><div class="abs dot" style="top:617px"></div><div class="abs dot" style="top:657px"></div>
<div class="abs scroll"></div><div class="abs thumb"></div>

<div class="abs f" style="top:457px"><span class="lab">Patent Title</span> : POLYCOMB-ASSOCIATED NON-CODING RNAS</div>
<div class="abs f" style="top:488px"><span class="lab">Abstract</span></div>
<div class="abs f" style="top:510px;width:640px;white-space:normal;line-height:22px">This invention relates to polycomb-associated long non-coding RNAs (lncRNAs), libraries and fragments of those ncRNAs, inhibitory nucleic acids and methods and compositions for targeting lncRNAs</div>
<div class="abs f" style="top:565px"><span class="lab">Patent assignee</span><span class="col">:</span><span class="val">MOREL, ET AL.;</span></div>
<div class="abs f" style="top:592px"><span class="lab">Normalized patent assignee</span><span class="col">:</span><span class="val">NORTHFIELD MEDICAL TRUST</span></div>
<div class="abs f" style="top:619px"><span class="lab">Normalized parent</span><span class="col">:</span><span class="val">NORTHFIELD MEDICAL TRUST</span></div>
<div class="abs f" style="top:646px"><span class="lab">Patent inventors</span><span class="col">:</span><span class="val" style="line-height:27px">MOREL ANNA T [US]; PRAVEC LENA [US]; OKAFOR RUTH [US];<br>HALVERSEN MARK [US]; DUVALL PETER KENDRICK [US]</span></div>
<div class="abs f" style="top:702px"><span class="lab">Patent classification</span><span class="col">:</span><span class="val" style="line-height:27px">International Classification: C07H 021/04;<br>US Classification: 536/024.31; 536/024.3; 536/023.1; 435/006; 435/091.2;<br>European Classification:</span></div>

<div class="abs side">
  Patent number : <a>WO2012087983</a><br>
  Application number : <a>WO2011US65939</a><br>
  Patent family : <a>WO2012065143; WO2012087983;</a><br>
  Patent family ID : <a>WO2012065143</a><br>
  Seq. listing equivalents : <a>WO2012087983;</a><br>
  Equivalents member type : <a>representative</a><br>
  PCT pub no : <a>WO2012087983</a><br>
  Link out : <a>PatScope, IPRegistry, Claimview details, Claimview PDF, MiniPatent, Open Patent Desk, PatVault, Lumen Innovation</a>
</div>

</body>
</html>
```